Website Design for new skincare product launch/rebranding

The Dew Meridian website is currently live and built through Pagevolt.com. While the existing site has served as a strong starting point, I’m now looking to elevate the overall experience with a complete redesign that reflects the growth and vision of the brand. This will be a full visual and functional revamp — not just a refresh — with the goal of creating a more elevated, intuitive, and conversion-focused platform. I’m looking for a designer who can not only reimagine the layout and visuals, but also collaborate on optimizing the user journey and site structure for both storytelling and sales.

Target Market(s)

Age 25- 45 (core), with secondary appeal to 18-55. Primarily women, but gender inclusive. Wellness/Holistic Beauty/Organic Ingredients, Botanical.

Industry/Entity Type

Beauty, aesthetics, wellness.

Number of Pages Required

5+ page

Font styles to use
Other font styles liked:
• Gravesned Sans Family

Colors

Designer to choose colors to be used in the design.

Requirements
Must have
• Include standard pages (Home, Our Story/Values, Shop, Product Detail with ingredients/description/etc., Contact) and any other recommended sections to optimize conversion. Minimal, clean, calming visual. Seamlessly integrate with Cartwell for all product sales.
Nice to have
• Company colors are attached in images, along with first two products that are launching. One called Velunmist, and one called Petravelle. Fonts and shapes need to align accordingly. Feel elevated, neutral, and luxe while maintaining a grounded, earthy minimalism. Visual inspiration includes brands like Lantern Grove, Marble Osprey, and TOvelin — minimal yet high-end, with thoughtful use of whitespace, typography, and subtle movement. Would LOVE to have movement (short clip GIF) on either the home page or ingredient page, reference TOvelin website (homepage or LuminWeave System™ Tab)
Should not have
• dark colors, complex design elements, too many different fonts. For ingredients, stick to botanical images and information only, with no mentions of CBD or use of leaf imagery.

```html
<!DOCTYPE html>
<html lang="en">
<head>
<meta charset="utf-8">
<title>Dew Meridian — Where Skin Meets Balance</title>
<link href="https://fonts.googleapis.com/css2?family=Lexend:wght@500;600&family=Poppins:wght@400;500;600&family=Cormorant+Garamond:wght@500&display=swap" rel="stylesheet">
<style>
:root{
  --ink:#1d1d1b;
  --text:#55534f;
  --stone:#9a9991;
  --stone-dark:#8d8c84;
  --sand:#dcd3cf;
  --sand-soft:#d8cfcb;
  --card:#f3f1ef;
  --line:#c9c7c2;
  --white:#ffffff;
}
*{box-sizing:border-box;margin:0;padding:0}
html,body{width:1200px;height:3839px;overflow:hidden;background:var(--white)}
body{position:relative;font-family:"Poppins",sans-serif;color:var(--text)}
.abs{position:absolute}
.heading{font-family:"Lexend",sans-serif;font-weight:600;color:var(--ink);letter-spacing:.04em;text-transform:uppercase}
.btn{position:absolute;display:flex;align-items:center;justify-content:center;background:var(--stone);color:var(--white);border-radius:40px;font-family:"Poppins",sans-serif;font-weight:600;font-size:12px;letter-spacing:.06em;text-transform:uppercase}
.rule{position:absolute;height:1.5px;background:var(--stone)}
.photo{position:absolute}

/* header */
.hero{position:absolute;left:0;top:0;width:1200px;height:705px;background:radial-gradient(ellipse at 30% 40%,#fafafa 0%,#efefee 55%,#e3e3e1 100%)}
.nav-line{position:absolute;height:1px;background:var(--line)}
.nav a{position:absolute;top:51px;font-size:12px;font-weight:600;color:var(--ink);letter-spacing:.03em;text-decoration:none}
.brand{position:absolute;left:500px;top:24px;width:200px;text-align:center;font-family:"Cormorant Garamond",serif;font-weight:500;font-size:22px;color:var(--ink);letter-spacing:.02em;text-transform:uppercase;line-height:1.1}
.brand .dot{display:block;width:26px;height:26px;border-radius:50%;background:var(--ink);margin:0 auto 6px}
.icon{position:absolute;top:50px}
.hero-eyebrow{left:91px;top:298px;font-size:12px;font-weight:600;color:var(--ink);letter-spacing:.03em}
.hero-title{left:91px;top:331px;font-size:35px;line-height:41px}
.hero-copy{left:872px;top:311px;width:250px;font-size:14px;line-height:22px}
.dots span{position:absolute;top:646px;width:10px;height:10px;border-radius:50%;background:#c9c8c4}

/* about */
.about-title{left:699px;top:918px;font-size:30px;line-height:34px}
.about-copy{left:699px;top:1022px;width:360px;font-size:13.5px;line-height:22.5px}

/* products */
.product-card{left:73px;top:1386px;width:563px;height:289px;background:var(--card);border-radius:10px}
.product-name{font-size:29px}
.product-copy{font-size:13.5px;line-height:22.5px;width:400px}
.bottle{border-radius:18px;background:linear-gradient(180deg,#ecebe8 0%,#cfcdc8 100%)}

/* science */
.science{left:0;top:1770px;width:1200px;height:587px;background:radial-gradient(ellipse at 70% 20%,#fbfbfa 0%,#efefed 55%,#e6e6e4 100%)}
.pillar-title{position:absolute;width:270px;text-align:center;font-size:14px;font-weight:600;color:var(--ink);letter-spacing:.04em;text-transform:uppercase}
.pillar-copy{position:absolute;text-align:center;font-size:13.5px;line-height:22.5px}
.pillar-icon{position:absolute;width:50px;height:50px;border-radius:50%;border:1.5px solid #cfcdc9;background:var(--white);display:flex;align-items:center;justify-content:center}

/* testimonial */
.quote-title{left:177px;top:2576px;font-size:30px;line-height:34px}
.quote-copy{left:177px;top:2670px;width:400px;font-size:13.5px;line-height:22.5px}
.quote-name{left:177px;top:2806px;font-size:13px;font-weight:600;color:var(--ink);letter-spacing:.04em}
.arrow{position:absolute;left:85px;width:32px;height:32px;border-radius:50%;display:flex;align-items:center;justify-content:center}

/* newsletter */
.email{left:362px;top:3108px;width:483px;height:57px;border:1.5px solid #8e8d87;border-radius:40px;padding-left:29px;display:flex;align-items:center;font-size:14px;color:var(--ink)}

/* journal */
.journal{left:0;top:3306px;width:1200px;height:233px;background:linear-gradient(90deg,#dcdcda 0%,#d3d3d1 50%,#dcdcda 100%)}

/* footer */
.foot-nav a{position:absolute;top:3713px;font-size:12.5px;font-weight:600;color:var(--ink);letter-spacing:.03em;text-decoration:none}
.social span{position:absolute;top:3780px;width:22px;height:22px;border-radius:50%;background:#9c9b95}
</style>
</head>
<body>

<section class="hero">
  <div class="nav-line" style="left:76px;top:28px;width:436px"></div>
  <div class="nav-line" style="left:688px;top:28px;width:437px"></div>
  <div class="nav-line" style="left:76px;top:86px;width:1049px"></div>
  <nav class="nav">
    <a style="left:114px">HOME</a>
    <a style="left:179px">OUR STORY</a>
    <a style="left:278px">SHOP</a>
    <a style="left:340px">PRODUCT DETAIL</a>
  </nav>
  <div class="brand"><span class="dot"></span>Dew Meridian</div>
  <svg class="icon" style="left:855px" width="12" height="12" viewBox="0 0 12 12" fill="none" stroke="#1d1d1b" stroke-width="1.6"><circle cx="5" cy="5" r="3.6"/><path d="M8 8l3 3"/></svg>
  <svg class="icon" style="left:894px" width="12" height="12" viewBox="0 0 12 12" fill="none" stroke="#1d1d1b" stroke-width="1.2"><circle cx="6" cy="3.5" r="2.5"/><path d="M1.5 11.5c0-3 2-4.5 4.5-4.5s4.5 1.5 4.5 4.5z"/></svg>
  <svg class="icon" style="left:932px" width="13" height="12" viewBox="0 0 13 12" fill="none" stroke="#1d1d1b" stroke-width="1.2"><path d="M1 1h2l1.5 7h6.5l1-5H4"/><circle cx="5.5" cy="10.5" r="1"/><circle cx="10" cy="10.5" r="1"/></svg>
  <div class="btn" style="left:974px;top:40px;width:121px;height:36px">Contact</div>

  <div class="abs hero-eyebrow">WELCOME TO DEW MERIDIAN</div>
  <h1 class="abs heading hero-title">Where<br>Skin Meets<br>Balance</h1>

  <div class="photo" role="img" aria-label="Photo of two serum dropper bottles with silver labels on a soft beige circular backdrop" style="left:377px;top:173px;width:446px;height:446px;border-radius:50%;background:radial-gradient(circle at 50% 45%,#e4ddd8 0%,#d5ccc7 65%,#c9c0bb 100%)"></div>

  <p class="abs hero-copy">Botanical beauty rituals, mindfully formulated to nourish, protect, and align your skin.</p>
  <div class="btn" style="left:872px;top:395px;width:198px;height:36px">Shop the Collection</div>

  <div class="dots">
    <span style="left:570px"></span>
    <span style="left:594px;width:14px;height:14px;top:644px;background:#fff;border:2px solid #9a9991"></span>
    <span style="left:620px"></span>
  </div>
</section>

<section>
  <svg class="abs" style="left:140px;top:800px" width="500" height="500" viewBox="0 0 500 500" fill="none" stroke="#a8a7a2" stroke-width="1.2"><circle cx="240" cy="262" r="234"/></svg>
  <div class="photo" role="img" aria-label="Portrait photo of a woman with short curly hair, soft neutral light" style="left:172px;top:820px;width:438px;height:438px;border-radius:50%;background:radial-gradient(circle at 45% 45%,#e6dbd2 0%,#d6c8bd 50%,#c8c4bf 100%)"></div>
  <div class="abs" style="left:454px;top:792px;width:150px;height:150px;border-radius:50%;background:var(--white);box-shadow:0 6px 24px rgba(0,0,0,.06)"></div>

  <h2 class="abs heading about-title">Elevated Skin<br>Wellness, Naturally</h2>
  <div class="rule" style="left:699px;top:992px;width:351px;background:#3a3936"></div>
  <p class="abs about-copy">At Dew Meridian, we believe that beauty blooms through balance. Our formulations are crafted with purpose — blending potent botanicals with modern skin science to support your skin’s rhythm, naturally.</p>
  <div class="btn" style="left:699px;top:1133px;width:197px;height:37px">Learn More About Us</div>
</section>

<section>
  <div class="abs product-card"></div>
  <div class="photo bottle" role="img" aria-label="Product photo of the Petravelle serum bottle" style="left:116px;top:1408px;width:78px;height:239px"></div>
  <h3 class="abs heading product-name" style="left:218px;top:1450px">Petravelle</h3>
  <div class="rule" style="left:218px;top:1492px;width:108px"></div>
  <p class="abs product-copy" style="left:218px;top:1510px">A moisture-balancing elixir infused with adaptogenic botanicals to restore skin harmony and barrier strength.</p>
  <div class="btn" style="left:218px;top:1571px;width:223px;height:36px">View Details / Add to Bag</div>

  <div class="photo bottle" role="img" aria-label="Product photo of the Velunmist serum bottle" style="left:686px;top:1408px;width:80px;height:248px"></div>
  <h3 class="abs heading product-name" style="left:788px;top:1450px">Velunmist</h3>
  <div class="rule" style="left:788px;top:1492px;width:108px"></div>
  <p class="abs product-copy" style="left:788px;top:1510px">A lightweight, botanical-based hydrating serum that delivers a glass-skin glow without the weight.</p>
  <div class="btn" style="left:788px;top:1571px;width:224px;height:36px">View Details / Add to Bag</div>
</section>

<section class="abs science">
  <h2 class="abs heading" style="left:0;top:80px;width:1200px;text-align:center;font-size:27px">Grounded in Nature, Backed by Science</h2>
  <div class="rule" style="left:548px;top:119px;width:105px"></div>

  <div class="abs" style="left:466px;top:152px;width:269px;height:352px;background:var(--sand-soft);border-radius:6px"></div>

  <div class="photo" role="img" aria-label="Photo of glass bottles of botanical oils among green plants" style="left:198px;top:167px;width:237px;height:145px;border-radius:6px;background:linear-gradient(135deg,#6f8a48 0%,#a3ae72 55%,#c9c7b3 100%)"></div>
  <div class="pillar-title" style="left:181px;top:322px">Botanical Ingredients</div>
  <p class="pillar-copy" style="left:196px;top:355px;width:240px">We source high-quality, plant-powered ingredients that are gentle, effective, and rooted in traditional healing practices.</p>
  <div class="pillar-icon" style="left:285px;top:464px"><svg width="20" height="22" viewBox="0 0 20 22" fill="none" stroke="#b5b3ae" stroke-width="1.3"><path d="M7 2h6M8 2v6L3 19h14L12 8V2"/></svg></div>

  <div class="photo" role="img" aria-label="Photo of amber apothecary bottles with herbal capsules and fresh greens" style="left:480px;top:167px;width:241px;height:145px;border-radius:6px;background:linear-gradient(135deg,#e6d8c6 0%,#c9976a 50%,#8fa462 100%)"></div>
  <div class="pillar-title" style="left:466px;top:322px;color:#fff">Holistic Formulations</div>
  <p class="pillar-copy" style="left:491px;top:355px;width:220px;color:#fff">Each product is thoughtfully blended to support skin health from all angles — balancing function, feel, and long-term results.</p>
  <div class="pillar-icon" style="left:579px;top:479px"><svg width="20" height="22" viewBox="0 0 20 22" fill="none" stroke="#b5b3ae" stroke-width="1.3"><path d="M8 2h4M9 2v4h2V2M7 6h6v14H7z"/></svg></div>

  <div class="photo" role="img" aria-label="Photo of hands holding soil against a soft green background" style="left:765px;top:167px;width:241px;height:145px;border-radius:6px;background:radial-gradient(circle at 50% 55%,#8aa95a 0%,#557c34 60%,#365627 100%)"></div>
  <div class="pillar-title" style="left:751px;top:322px">Sustainable Practices</div>
  <p class="pillar-copy" style="left:766px;top:355px;width:240px">From packaging to production, we prioritize practices that are kind to the earth and respectful of your skin.</p>
  <div class="pillar-icon" style="left:861px;top:464px"><svg width="20" height="20" viewBox="0 0 20 20" fill="none" stroke="#b5b3ae" stroke-width="1.3"><circle cx="10" cy="10" r="7"/><path d="M6 10l3 3 5-6"/></svg></div>
</section>

<section>
  <svg class="abs" style="left:175px;top:2500px" width="80" height="62" viewBox="0 0 80 62" fill="#d8cfcb"><path d="M0 30C0 12 10 2 28 0l2 8C20 11 16 17 16 24h14v38H0zM44 30C44 12 54 2 72 0l2 8c-10 3-14 9-14 16h14v38H44z"/></svg>
  <h2 class="abs heading quote-title">What Our<br>Community Is Saying</h2>
  <div class="arrow" style="top:2669px;background:var(--stone)"><svg width="12" height="10" viewBox="0 0 12 10" fill="none" stroke="#fff" stroke-width="1.2"><path d="M11 5H1M5 1L1 5l4 4"/></svg></div>
  <div class="arrow" style="top:2711px;background:#e6e5e2"><svg width="12" height="10" viewBox="0 0 12 10" fill="none" stroke="#fff" stroke-width="1.2"><path d="M1 5h10M7 1l4 4-4 4"/></svg></div>
  <p class="abs quote-copy">After using Velunmist for just a week, my skin looks noticeably brighter and more even. It feels like a reset for my face. My skin has always been sensitive, but Petravelle calmed the redness without feeling heavy. It’s the only moisturizer I trust now</p>
  <div class="abs quote-name">MARA T SENSITIVE SKIN</div>

  <svg class="abs" style="left:640px;top:2440px" width="480" height="490" viewBox="0 0 480 490" fill="none" stroke="#a8a7a2" stroke-width="1.2"><circle cx="240" cy="246" r="232"/></svg>
  <div class="photo" role="img" aria-label="Portrait photo of a woman in a cream sweater in a calm meditation pose" style="left:652px;top:2457px;width:440px;height:440px;border-radius:50%;background:radial-gradient(circle at 50% 40%,#efebe7 0%,#e1dfdc 55%,#d4d3d0 100%)"></div>
</section>

<section>
  <h2 class="abs heading" style="left:0;top:3003px;width:1200px;text-align:center;font-size:29px">Let’s Stay Aligned</h2>
  <div class="rule" style="left:548px;top:3055px;width:105px"></div>
  <p class="abs" style="left:0;top:3069px;width:1200px;text-align:center;font-size:13.5px;color:var(--ink)">Be the first to know about new launches, rituals, and exclusive offers.</p>
  <div class="abs email">Email Address</div>
  <div class="btn" style="left:362px;top:3174px;width:483px;height:57px">Subscribe</div>
</section>

<section class="abs journal" role="img" aria-label="Soft grey band with a faded photo of a woman applying serum">
  <h2 class="abs heading" style="left:192px;top:77px;font-size:29px">Knowledge Is a Ritual</h2>
  <p class="abs" style="left:191px;top:119px;width:380px;font-size:13.5px;line-height:22.5px;color:var(--ink)">Explore mindful skincare tips, ingredient insights, and daily wellness rituals in our journal.</p>
  <div class="btn" style="left:785px;top:96px;width:224px;height:36px;background:var(--stone-dark)">Read the Journal</div>
</section>

<footer>
  <div class="abs" style="left:168px;top:3630px;width:28px;height:28px;border-radius:50%;background:var(--sand)"></div>
  <div class="abs" style="left:76px;top:3690px;font-family:'Cormorant Garamond',serif;font-weight:500;font-size:36px;color:var(--sand);letter-spacing:.02em;text-transform:uppercase">Dew Meridian</div>
  <nav class="foot-nav">
    <a style="left:702px">HOME</a>
    <a style="left:766px">OUR STORY</a>
    <a style="left:866px">SHOP</a>
    <a style="left:927px">PRODUCT DETAIL</a>
    <a style="left:1063px">CONTACT</a>
  </nav>
  <div class="abs" style="left:76px;top:3760px;width:1049px;height:1px;background:var(--line)"></div>
  <div class="abs" style="left:76px;top:3784px;font-size:11.5px;font-weight:600;color:var(--ink);letter-spacing:.03em">COPYRIGHT 2025 ALL RIGHTS RESERVED</div>
  <div class="social">
    <span style="left:1013px"></span>
    <span style="left:1043px"></span>
    <span style="left:1073px"></span>
    <span style="left:1103px"></span>
  </div>
</footer>

</body>
</html>
```